Distribution/Printing company needs a web site to inform prospective customers on what we do.

Distribution/Printing/Packaging company needs a web site to inform prospective customers on what we do. Please look at our direct to consumer web site (under development) for an idea of the product lines we sell: storedev.kelbrynwares.com
Logo files are attached as is a flyer that is under development which contains other information about the company (this is to be used for content- not to be posted as is). The web site should be focused on our business customer base and is not intended to be direct to consumer. Site should have a link to our consumer web site.
Site design should be mobile friendly, or mobile could be redirected to a mobile version. This web site will be strictly informational and will not be designed for any sales transactions.

Manufacturing and retail businesses, any other multi-site business that would benefit from centralized pricing and budget controls we can provide (banks, medical/dental offices, educational facilities, etc).

• 1) Top level menu: Products, about us, locations, contact us, news
• 2) page with news/promotions that is easily updated
• 3) "contact us" form (name, company, phone, email address) email link
• 4) link to www.store.kelbrynwares.com with information that lower pricing is available for businesses
• 5) SEO keywords
• 6) Link to powerpoint presentation file
• 1) our phone number should appear on every page near the top

```html
<!DOCTYPE html>
<html lang="en">
<head>
<meta charset="utf-8">
<title>Kelbryn Supply – Packaging, Printing, Distribution</title>
<link rel="stylesheet" href="https://fonts.googleapis.com/css2?family=Open+Sans:wght@300;400;600;700;800&display=swap">
<style>
:root{
  --ink:#2b2b2b;
  --dark:#2e2e2e;
  --band:#555555;
  --light:#f1f0f3;
  --white:#ffffff;
  --muted:#8a8a8a;
  --faint:#c4c4c4;
  --icon-bg:#e4e4e4;
  --blue:#1b8fd6;
  --red:#d0202a;
  --border:#c9c9c9;
  --rule:#cfcfcf;
}
*{margin:0;padding:0;box-sizing:border-box}
html,body{width:1200px;height:2917px;overflow:hidden}
body{font-family:"Open Sans",Arial,sans-serif;color:var(--ink);background:var(--white);position:relative}
section,header,footer{position:absolute;left:0;width:1200px}

/* header */
.site-header{top:0;height:171px;background:var(--dark);color:var(--white)}
.brand{position:absolute;left:470px;top:46px;width:260px;text-align:center}
.brand-mark{display:block;margin:0 auto 12px;width:28px;height:28px;border-radius:50%;background:var(--white)}
.brand-name{font-size:20px;font-weight:700;letter-spacing:1px;line-height:24px}
.brand-tag{font-size:12px;font-weight:600;line-height:16px;margin-top:2px}
.rule{position:absolute;top:97px;height:14px;border-top:2px solid var(--rule);border-bottom:2px solid var(--rule)}
.rule::after{content:"";position:absolute;left:0;right:0;top:4px;border-top:2px solid var(--rule)}
.rule-left{left:99px;width:374px}
.rule-right{left:727px;width:374px}
.nav{position:absolute;top:130px;list-style:none;display:flex;font-size:13px;font-weight:600}
.nav-left{left:157px;gap:52px}
.nav-right{left:762px;gap:52px}
.support{position:absolute;right:97px;top:6px;display:flex;gap:10px;align-items:flex-start}
.support-label{font-size:15px;text-decoration:underline;letter-spacing:.5px}
.support-phone{font-size:25px;line-height:1}

/* hero */
.hero{top:171px;height:587px;background:linear-gradient(180deg,#7d8a96 0%,#9aa7b3 35%,#6d86a4 60%,#b09a7c 100%)}
.hero-arrow{position:absolute;top:250px}
.hero-arrow.prev{left:36px}
.hero-arrow.next{right:36px}
.hero-caption{position:absolute;left:97px;top:407px;width:996px;height:148px;background:rgba(50,50,50,.72);color:var(--white);padding:18px 22px}
.hero-caption h2{font-size:35px;font-weight:700}
.hero-caption p{font-size:13px;line-height:20px;margin-top:6px}
.dots{position:absolute;left:570px;top:527px;display:flex;gap:5px}
.dots span{width:17px;height:17px;border-radius:50%;background:var(--white)}

/* mission */
.mission{top:758px;height:195px;background:var(--dark);color:var(--white);padding:44px 97px}
.mission h2{font-size:32px;font-weight:700}
.mission p{font-size:14px;line-height:38px;margin-top:8px}

/* about */
.about{top:953px;height:753px;background:var(--white)}
.section-title{text-align:center;font-size:60px;font-weight:300}
.about .section-title{margin-top:50px}
.section-lede{width:960px;margin:12px auto 0;text-align:center;color:var(--faint);font-size:18px;line-height:26px}
.feature{position:absolute;width:340px}
.feature h3{font-size:24px;font-weight:700;text-transform:uppercase}
.feature p{font-size:14.5px;line-height:25.5px;color:var(--muted);margin-top:20px}
.feature.left{left:117px;text-align:right}
.feature.right{left:743px}
.icon-circle{position:absolute;width:108px;height:108px;border-radius:50%;background:var(--icon-bg);display:flex;align-items:center;justify-content:center}

/* testimonials */
.testimonials{top:1706px;height:453px;background:var(--light)}
.testimonials .section-title{margin-top:34px}
.quote-card{position:absolute;top:177px;width:490px;height:212px;border:2px solid var(--border);background:var(--light)}
.quote-photo{position:absolute;left:-6px;top:-6px;width:212px;height:212px;border-radius:50%;border:3px solid #777;background:linear-gradient(135deg,#8a7868,#d8cfc4 55%,#6f6a67)}
.quote-text{position:absolute;left:229px;top:24px;width:215px;font-size:15.5px;line-height:22px;color:#555}
.quote-author{position:absolute;left:229px;top:157px;display:flex;align-items:center;gap:12px;font-size:15.5px;color:var(--blue)}

/* newsletter */
.newsletter{top:2159px;height:97px;background:var(--band);color:var(--white)}
.newsletter h2{position:absolute;left:97px;top:27px;font-size:30px;font-weight:800}
.email-field{position:absolute;left:532px;top:18px;width:326px;height:62px;background:#f5f5f5;color:#999;font-size:16px;display:flex;align-items:center;justify-content:center}
.subscribe{position:absolute;left:903px;top:14px;width:200px;height:70px;border-top:2px solid var(--white);border-bottom:2px solid var(--white);font-size:15px;font-weight:700;display:flex;align-items:center;justify-content:center}

/* video */
.video{top:2256px;height:370px;background:var(--dark);color:var(--white)}
.video-frame{position:absolute;left:99px;top:43px;width:508px;height:288px;background:linear-gradient(160deg,#8d7a5c,#b99f76 45%,#5d5348)}
.video-bar{position:absolute;left:0;bottom:0;width:100%;height:42px;background:#1a1a1a}
.video-progress{position:absolute;left:40px;top:19px;width:410px;height:4px;background:#666}
.video-progress i{display:block;width:155px;height:4px;background:var(--red)}
.video-side{position:absolute;left:655px;top:32px;width:450px}
.video-side h2{font-size:32px;font-weight:400;line-height:1}
.video-side h3{font-size:15px;font-weight:400;margin-top:6px}
.clip{display:flex;gap:18px;margin-top:10px;position:relative;height:70px}
.clip:first-of-type{margin-top:14px}
.clip-thumb{flex:none;width:90px;height:70px;border:2px solid #ddd;background:linear-gradient(135deg,#7a6a55,#b8a283)}
.clip-num{position:absolute;left:75px;top:20px;width:30px;height:30px;border-radius:50%;background:var(--red);border:3px solid #222;font-size:14px;font-weight:700;display:flex;align-items:center;justify-content:center}
.clip-title{font-size:15.5px;line-height:20px;margin-top:4px}
.clip-sub{font-size:12px;line-height:18px;margin-top:2px}
.clip-more{font-size:11px;line-height:14px;color:#555}

/* social feed */
.feed{top:2626px;height:120px;background:var(--band)}
.feed-box{position:absolute;left:97px;top:16px;width:1006px;height:90px;background:var(--dark);border-radius:4px;color:var(--white);display:flex;align-items:center;padding:0 20px 0 25px;gap:30px}
.feed-dot{flex:none;width:50px;height:50px;border-radius:50%;background:var(--white)}
.feed-box p{font-size:13.5px;line-height:24px}
.feed-box a{color:#e4d23c}

/* follow */
.follow{top:2746px;height:113px;background:var(--white)}
.follow-item{position:absolute;top:28px;display:flex;gap:18px;align-items:center}
.follow-dot{width:60px;height:60px;border-radius:50%;background:var(--dark)}
.follow-dot.accent{background:#1565a8}
.follow-title{font-size:15px;color:#555}
.follow-sub{font-size:12px;color:#bbb}

/* footer */
.site-footer{top:2859px;height:58px;background:var(--band);color:var(--white);font-size:11px}
.site-footer .copy{position:absolute;left:97px;top:22px}
</style>
</head>
<body>

<header class="site-header">
  <ul class="nav nav-left"><li>HOME</li><li>ABOUT US</li><li>PRODUCTS</li></ul>
  <div class="rule rule-left"></div>
  <div class="brand">
    <span class="brand-mark"></span>
    <div class="brand-name">KELBRYN SUPPLY</div>
    <div class="brand-tag">Packaging • Printing • Distribution</div>
  </div>
  <div class="rule rule-right"></div>
  <ul class="nav nav-right"><li>NEWS</li><li>LOCATIONS</li><li>CONTACT US</li></ul>
  <div class="support">
    <svg width="40" height="44" viewBox="0 0 40 44" aria-hidden="true"><path d="M6 22a14 14 0 0 1 28 0" fill="none" stroke="#fff" stroke-width="3"/><rect x="3" y="20" width="8" height="13" rx="3" fill="#fff"/><rect x="29" y="20" width="8" height="13" rx="3" fill="#fff"/><path d="M33 33q0 7-10 8" fill="none" stroke="#fff" stroke-width="2"/><circle cx="21" cy="41" r="2.5" fill="#fff"/></svg>
    <div><div class="support-label">CUSTOMER SUPPORT</div><div class="support-phone">222 048 7310</div></div>
  </div>
</header>

<section class="hero" role="img" aria-label="Packaging plant floor with blue machinery and stacked cardboard boxes">
  <svg class="hero-arrow prev" width="34" height="56" viewBox="0 0 34 56" aria-hidden="true"><path d="M28 4 6 28l22 24" fill="none" stroke="#fff" stroke-width="8"/></svg>
  <svg class="hero-arrow next" width="34" height="56" viewBox="0 0 34 56" aria-hidden="true"><path d="M6 4l22 24L6 52" fill="none" stroke="#fff" stroke-width="8"/></svg>
  <div class="hero-caption">
    <h2>Packaging</h2>
    <p>Lorem ipsum dolor sit amet conse ctetur adipisicing elit, sed do eiusmod tempor incididunt ut labore et dolore magna aliqua. Ut enim ad minim veniam, quis nostrud exercitation ullamco laboris nisi ut aliquip ex ea commodo consequat. Duis aute irure dolo.</p>
  </div>
  <div class="dots"><span></span><span></span><span></span></div>
</section>

<section class="mission">
  <h2>Let's preserve our world together!</h2>
  <p>Our Company is one of the leading recycling, renewable energy and waste management companies. We work with more than 90 local authorities and thousands of private cusatomers across the country.</p>
</section>

<section class="about">
  <h2 class="section-title">About Us</h2>
  <p class="section-lede">Sed ut perspiciatis unde omnis iste natus error sit voluptatem accusantium doloremque laudantium, totam rem aperiam, eaque ipsa quae.</p>

  <div class="feature left" style="top:261px"><h3>Perspiciatis unde</h3><p>Sed ut perspiciatis unde omnis iste natus error sit voluptatem accusantium doloremque laudantium, totam rem aperiam, eaque ipsa quae ab illo inventore veritatis et architecto beatae vitae dicta sunt explicabo.</p></div>
  <div class="icon-circle" style="left:481px;top:266px"><svg width="60" height="50" viewBox="0 0 60 50" aria-hidden="true"><rect x="4" y="4" width="46" height="32" rx="3" fill="none" stroke="#333" stroke-width="4"/><rect x="12" y="12" width="20" height="3" fill="#333"/><rect x="12" y="19" width="26" height="3" fill="#333"/><rect x="20" y="38" width="14" height="6" fill="#333"/><path d="M40 26l14 8-6 2 4 8-3 2-4-8-5 4z" fill="#333"/></svg></div>
  <div class="icon-circle" style="left:611px;top:266px"><svg width="44" height="56" viewBox="0 0 44 56" aria-hidden="true"><rect x="4" y="2" width="30" height="48" rx="3" fill="none" stroke="#333" stroke-width="4"/><rect x="10" y="8" width="18" height="9" fill="#333"/><g fill="#333"><rect x="10" y="22" width="5" height="5"/><rect x="19" y="22" width="5" height="5"/><rect x="10" y="31" width="5" height="5"/><rect x="19" y="31" width="5" height="5"/><rect x="10" y="40" width="5" height="5"/></g><circle cx="32" cy="38" r="3" fill="#333"/><circle cx="41" cy="50" r="3" fill="#333"/><path d="M42 36 30 52" stroke="#333" stroke-width="3"/></svg></div>
  <div class="feature right" style="top:261px"><h3>Voluptatem accus</h3><p>Sed ut perspiciatis unde omnis iste natus error sit voluptatem accusantium doloremque laudantium, totam rem aperiam, eaque ipsa quae ab illo inventore veritatis et architecto beatae vitae dicta sunt explicabo.</p></div>

  <div class="feature left" style="top:481px"><h3>Omnis iste natus</h3><p>Sed ut perspiciatis unde omnis iste natus error sit voluptatem accusantium doloremque laudantium, totam rem aperiam, eaque ipsa quae ab illo inventore veritatis et architecto beatae vitae dicta sunt explicabo.</p></div>
  <div class="icon-circle" style="left:481px;top:486px"><svg width="60" height="52" viewBox="0 0 60 52" aria-hidden="true"><g fill="#333"><circle cx="14" cy="16" r="6"/><circle cx="30" cy="12" r="7"/><circle cx="46" cy="16" r="6"/><rect x="8" y="24" width="12" height="26" rx="3"/><rect x="23" y="21" width="14" height="29" rx="3"/><rect x="40" y="24" width="12" height="26" rx="3"/></g></svg></div>
  <div class="icon-circle" style="left:611px;top:486px"><svg width="56" height="56" viewBox="0 0 56 56" aria-hidden="true"><rect x="6" y="4" width="30" height="42" rx="3" fill="none" stroke="#333" stroke-width="4"/><circle cx="32" cy="30" r="10" fill="#e4e4e4" stroke="#333" stroke-width="4"/><path d="M39 37l10 10" stroke="#333" stroke-width="6" stroke-linecap="round"/></svg></div>
  <div class="feature right" style="top:481px"><h3>Laudantium, totam</h3><p>Sed ut perspiciatis unde omnis iste natus error sit voluptatem accusantium doloremque laudantium, totam rem aperiam, eaque ipsa quae ab illo inventore veritatis et architecto beatae vitae dicta sunt explicabo.</p></div>
</section>

<section class="testimonials">
  <h2 class="section-title">Testimonials</h2>
  <article class="quote-card" style="left:111px">
    <div class="quote-photo" role="img" aria-label="Portrait of a smiling client couple"></div>
    <p class="quote-text">Aenean nonummy hendrerit mau phasellu porta. Fusce suscipit varius mi sed. Cum sociis natoque penatibus et magnis dis parturient montes,</p>
    <div class="quote-author"><svg width="26" height="24" viewBox="0 0 26 24" aria-hidden="true"><path d="M13 2C6 2 1 6 1 11c0 3 2 5 4 7l-2 5 6-3c1 0 3 1 4 1 7 0 12-4 12-10S20 2 13 2z" fill="var(--blue)"/></svg>Tom Hartwell</div>
  </article>
  <article class="quote-card" style="left:615px">
    <div class="quote-photo" role="img" aria-label="Portrait of a smiling client pair"></div>
    <p class="quote-text">Aenean nonummy hendrerit mau phasellu porta. Fusce suscipit varius mi sed. Cum sociis natoque penatibus et magnis dis parturient montes,</p>
    <div class="quote-author"><svg width="26" height="24" viewBox="0 0 26 24" aria-hidden="true"><path d="M13 2C6 2 1 6 1 11c0 3 2 5 4 7l-2 5 6-3c1 0 3 1 4 1 7 0 12-4 12-10S20 2 13 2z" fill="var(--blue)"/></svg>Lena Westmore</div>
  </article>
</section>

<section class="newsletter">
  <h2>NEWSLETTER SIGN UP:</h2>
  <div class="email-field">Your email</div>
  <div class="subscribe">SUBSCRIBE</div>
</section>

<section class="video">
  <div class="video-frame" role="img" aria-label="Warehouse video still with staff packing boxes">
    <div class="video-bar">
      <svg style="position:absolute;left:14px;top:15px" width="10" height="12" viewBox="0 0 10 12" aria-hidden="true"><path d="M0 0l10 6-10 6z" fill="#fff"/></svg>
      <div class="video-progress"><i></i></div>
      <svg style="position:absolute;right:14px;top:12px" width="18" height="18" viewBox="0 0 18 18" aria-hidden="true"><path d="M1 6V1h5M12 1h5v5M17 12v5h-5M6 17H1v-5" fill="none" stroke="#fff" stroke-width="2"/></svg>
    </div>
  </div>
  <div class="video-side">
    <h2>Featured Video</h2>
    <h3>Mollis Ipsum Tortor Vulputate</h3>
    <div class="clip"><div class="clip-thumb" role="img" aria-label="Clip thumbnail of warehouse work"></div><span class="clip-num">1</span><div><div class="clip-title">Lorem ipsum dolor sit amet, consectetur</div><div class="clip-sub">adipiscing eliteger gravida velit quis dolo</div><div class="clip-more">Read More</div></div></div>
    <div class="clip"><div class="clip-thumb" role="img" aria-label="Clip thumbnail of packing line"></div><span class="clip-num">2</span><div><div class="clip-title">Lorem ipsum dolor sit amet, consectetur</div><div class="clip-sub">adipiscing eliteger gravida velit quis dolo</div><div class="clip-more">Read More</div></div></div>
    <div class="clip"><div class="clip-thumb" role="img" aria-label="Clip thumbnail of stacked boxes"></div><span class="clip-num">3</span><div><div class="clip-title">Lorem ipsum dolor sit amet, consectetur</div><div class="clip-sub">adipiscing eliteger gravida velit quis dolo</div><div class="clip-more">Read More</div></div></div>
  </div>
</section>

<section class="feed">
  <div class="feed-box">
    <span class="feed-dot"></span>
    <p>Donec nec justo eget felis facilisis fermentum. Aliquam porttitor mauris sit amet orci. Aenean dignissim pellentesque felis euismod.Aliquam porttitor mauris sit amet orci. Aenean dignissim pellentesque felis euismod. <a>@kelbrynsupply</a></p>
  </div>
</section>

<section class="follow">
  <div class="follow-item" style="left:97px"><span class="follow-dot accent"></span><div><div class="follow-title">Follow us on Friendwall</div><div class="follow-sub">Faucibus tortor mentus</div></div></div>
  <div class="follow-item" style="left:476px"><span class="follow-dot"></span><div><div class="follow-title">Follow us on Circlesphere</div><div class="follow-sub">Faucibus tortor mentus</div></div></div>
  <div class="follow-item" style="left:876px"><span class="follow-dot"></span><div><div class="follow-title">Follow us on Workline</div><div class="follow-sub">Faucibus tortor mentus</div></div></div>
</section>

<footer class="site-footer">
  <span class="copy">Copyright © 2014 - All Rights Reserved</span>
</footer>

</body>
</html>
```